Stationary Design needed for Physical Therapy and Wellness Center

Letterhead, Envelopes, Business Cards (x2) needed. We are a studio specializing in helping our clients improve mobility, fitness, and recover from injury. We use the Spirolane method and need to adhere to their trademark restrictions.

Target Market(s)

Potential Clients: active people...many from dance or athletic backgrounds.

Industry/Entity Type

Health And Wellness

Font styles to use
Sans Serif
Other font styles liked:
• Times New Roman for the word Spirolane.

Colors
00a990
33b8a4
86cfc6
0393ce
33a6d7
85cae6

Requirements
Must have
• Attention to Spirolane trademark guidelines (Times New Roman font, Bold type, use of registered trademark symbol). Examples of current stationary can be provided as an example.
• Concept of movement, flow.

```html
<!DOCTYPE html>
<html lang="en">
<head>
<meta charset="utf-8">
<title>Letterhead</title>
<link href="https://fonts.googleapis.com/css2?family=Montserrat:wght@300&display=swap" rel="stylesheet">
<style>
  :root {
    --backdrop: #d3d9da;
    --paper: #ffffff;
    --teal-deep: #00a990;
    --teal-mid: #33b8a4;
    --shade-dark: #2a2a2a;
    --shade-light: #b8b8b8;
    --watermark: #e6e8e8;
  }
  html, body {
    margin: 0;
    width: 1200px;
    height: 784px;
    overflow: hidden;
    background: var(--backdrop);
  }
  .canvas {
    width: 1200px;
    height: 784px;
    display: flex;
    align-items: center;
    justify-content: center;
  }
  .letterhead {
    position: relative;
    width: 504px;
    height: 712px;
    background: var(--paper);
    box-shadow: 0 4px 18px rgba(0,0,0,0.12);
    overflow: hidden;
  }
  .letterhead__corners {
    position: absolute;
    inset: 0;
    width: 100%;
    height: 100%;
  }
  .letterhead__mark {
    position: absolute;
    left: 0;
    right: 0;
    top: 470px;
    display: flex;
    align-items: center;
    justify-content: center;
    gap: 14px;
  }
  .letterhead__mark-dot {
    width: 46px;
    height: 46px;
    border-radius: 50%;
    background: var(--watermark);
    flex: none;
  }
  .letterhead__mark-name {
    font-family: "Montserrat", sans-serif;
    font-weight: 300;
    font-size: 34px;
    letter-spacing: 2px;
    color: var(--watermark);
    white-space: nowrap;
  }
</style>
</head>
<body>
<main class="canvas">
  <section class="letterhead" aria-label="Letterhead">
    <svg class="letterhead__corners" viewBox="0 0 504 712" aria-hidden="true">
      <defs>
        <linearGradient id="teal-fold" x1="0" y1="0" x2="1" y2="1">
          <stop offset="0" stop-color="var(--teal-deep)"/>
          <stop offset="1" stop-color="var(--teal-mid)"/>
        </linearGradient>
        <linearGradient id="dark-fold" x1="0" y1="0" x2="1" y2="1">
          <stop offset="0" stop-color="var(--shade-light)"/>
          <stop offset="1" stop-color="var(--shade-dark)"/>
        </linearGradient>
      </defs>
      <path class="fold fold--top" d="M310 0 L504 0 L504 200 C450 100 390 20 310 0 Z" fill="url(#teal-fold)"/>
      <path class="fold fold--bottom" d="M0 500 L0 712 L190 712 C100 670 30 600 0 500 Z" fill="url(#dark-fold)"/>
    </svg>
    <div class="letterhead__mark">
      <span class="letterhead__mark-dot"></span>
      <span class="letterhead__mark-name">Arcwell Studio</span>
    </div>
  </section>
</main>
</body>
</html>
```